Property investment company needs a letterhead design!

We are a new residential and commercial property investment company. Name of the company is Morvesta Group, LLC. We have a new logo and now we need letterhead! We prefer to have a professional and upscale appearance. We don't have any fixed requirements, so be creative! Thank you for considering this project. We are so excited to see what happens!

Target Market(s)

Professional

Industry/Entity Type

Real Estate Development

```html
<!DOCTYPE html>
<html lang="en">
<head>
<meta charset="utf-8">
<title>Morvesta Group, LLC — Letterhead</title>
<link rel="stylesheet" href="https://fonts.googleapis.com/css2?family=Open+Sans:wght@400;600;700&family=Great+Vibes&display=swap">
<style>
  :root {
    --backdrop: #e6e7e9;
    --paper: #ffffff;
    --ink: #1f1f21;
    --spine: #202022;
    --rail: #dcdde0;
    --accent: #00aeef;
    --navy: #0f2340;
    --pattern-light: #f6f6f7;
    --pattern-dark: #e2e3e5;
  }
  * { margin: 0; padding: 0; box-sizing: border-box; }
  html, body { width: 1200px; height: 1200px; overflow: hidden; background: var(--backdrop); }
  body { font-family: "Open Sans", Arial, sans-serif; color: var(--ink); }

  .letterhead {
    position: absolute; left: 193px; top: 30px;
    width: 813px; height: 1140px;
    background: var(--paper);
    overflow: hidden;
    box-shadow: 0 10px 30px rgba(0,0,0,.12);
  }
  .spine { position: absolute; left: 0; top: 0; width: 41px; height: 100%; background: var(--spine); }
  .rail { position: absolute; left: 44px; top: 0; width: 25px; height: 100%; }
  .header-texture { position: absolute; left: 239px; top: 0; width: 574px; height: 330px; }

  .brand { position: absolute; left: 105px; top: 150px; display: flex; align-items: center; gap: 8px; }
  .brand-dot { width: 20px; height: 20px; border-radius: 50%; background: var(--navy); }
  .brand-name { font-weight: 700; font-size: 16px; color: var(--navy); letter-spacing: .3px; }

  .sender { position: absolute; left: 105px; top: 286px; }
  .sender-name { font-size: 13.5px; color: var(--accent); line-height: 18px; }
  .sender-role { font-size: 10px; line-height: 14px; margin-top: 1px; }
  .contact-list { margin-top: 5px; font-size: 11.5px; }
  .contact-row { height: 20px; line-height: 20px; white-space: nowrap; }
  .contact-key { display: inline-block; width: 26px; font-weight: 600; color: var(--accent); }
  .contact-key.dark { color: var(--ink); }

  .date { position: absolute; right: 105px; top: 343px; font-size: 11.5px; line-height: 20px; }

  .body-copy { position: absolute; left: 105px; top: 404px; width: 610px; font-size: 12px; }
  .paragraph { margin-bottom: 26px; }
  .paragraph div { height: 26px; line-height: 26px; white-space: nowrap; }

  .signoff { position: absolute; left: 105px; top: 826px; }
  .signature { font-family: "Great Vibes", cursive; font-size: 26px; line-height: 32px; }
  .signoff-name { font-weight: 700; font-size: 12.5px; line-height: 15px; }
  .signoff-role { font-size: 12px; line-height: 15px; }

  .footer-contacts { position: absolute; left: 93px; font-size: 12px; line-height: 15px; }
  .footer-phone { top: 975px; font-size: 11.5px; }
  .footer-address { top: 1022px; }
  .footer-web { top: 1066px; }
</style>
</head>
<body>
<main class="letterhead">
  <div class="spine"></div>

  <svg class="rail" viewBox="0 0 25 1140" preserveAspectRatio="none">
    <rect width="25" height="1140" fill="var(--rail)"/>
    <polygon points="0,953 25,927 25,1140 0,1140" fill="var(--accent)"/>
    <rect x="0" y="1011" width="25" height="2" fill="#fff"/>
    <rect x="0" y="1059" width="25" height="2" fill="#fff"/>
    <!-- phone -->
    <path d="M8.5 978 l2.5 -1 l1.8 3.2 l-1.6 1.2 q1 2.3 3 3.6 l1.3 -1.5 l3.1 1.9 l-1 2.4 q-6 0.4 -9.1 -9.8z" fill="#fff"/>
    <path d="M15 977 q3.5 0.6 4.3 4.3 M15 979.3 q1.7 0.4 2.1 2.1" stroke="#fff" stroke-width="1" fill="none"/>
    <!-- pin -->
    <path d="M12.5 1028 a5 5 0 0 1 5 5 c0 3.6 -5 9 -5 9 s-5 -5.4 -5 -9 a5 5 0 0 1 5 -5z" fill="#fff"/>
    <circle cx="12.5" cy="1033" r="1.8" fill="var(--accent)"/>
    <!-- globe -->
    <circle cx="12.5" cy="1081" r="6.5" stroke="#fff" stroke-width="1.4" fill="none"/>
    <path d="M6 1081 h13 M12.5 1074.5 q-4 6.5 0 13 M12.5 1074.5 q4 6.5 0 13" stroke="#fff" stroke-width="1.1" fill="none"/>
  </svg>

  <svg class="header-texture" viewBox="0 0 574 330" role="img" aria-label="Soft grey geometric tile texture fading into the header">
    <defs>
      <linearGradient id="texture-fill" x1="0" y1="0" x2="1" y2="1">
        <stop offset="0" stop-color="var(--pattern-light)"/>
        <stop offset=".45" stop-color="var(--pattern-dark)"/>
        <stop offset="1" stop-color="var(--pattern-light)"/>
      </linearGradient>
    </defs>
    <polygon points="0,0 574,0 574,270 515,330 430,250 380,305 270,195 190,270 0,120" fill="url(#texture-fill)" opacity=".9"/>
  </svg>

  <div class="brand">
    <span class="brand-dot"></span>
    <span class="brand-name">Morvesta Group, LLC</span>
  </div>

  <section class="sender">
    <div class="sender-name">Daniel Hartwell</div>
    <div class="sender-role">Chief Director</div>
    <div class="contact-list">
      <div class="contact-row"><span class="contact-key">A :</span>45-1,Lorem Road State - 8989</div>
      <div class="contact-row"><span class="contact-key dark">W :</span>email@mailid.com, www.myweb.com</div>
      <div class="contact-row"><span class="contact-key">P :</span>+880 - 12345 - 6789</div>
    </div>
  </section>

  <div class="date">Date, 06 May, 2021</div>

  <article class="body-copy">
    <div class="paragraph">
      <div>This is a sample letter that has been placed to demonstrate typing remat (Your Company). letterhead</div>
      <div>design. When positioned properly, it will serve to work in harmony with all other elements letterhead.</div>
      <div>This letterhead design is meant to project an image</div>
    </div>
    <div class="paragraph">
      <div>This letterhead design is meant project an image of professionalism reliability. By using simple aligen</div>
      <div>we have created a very spacious feeling. The simplicity suggest &nbsp;rengththe spaciousnes contributes h</div>
      <div>aesthetics the layout. These basic qualities along with the (Your Company)</div>
    </div>
    <div class="paragraph">
      <div>look and helps reinforce the (Your Company) brand. letterhead design is meant to project an image p</div>
      <div>design. When positioned properly, it will serve to work in harmony all the other elements letterhead.</div>
      <div>sionalism and reliability.</div>
    </div>
    <div class="paragraph">
      <div>This letterhead design is based on the (Form of your logo) form (Your Company) logo. Each stationery</div>
      <div>we have created a very spacious feeling. The simplicity suggests strength the spaciousnes contribute</div>
      <div>part of the (Form of your logo).</div>
    </div>
  </article>

  <section class="signoff">
    <div class="signature">Daniel Hartwell</div>
    <div class="signoff-name">Daniel Hartwell</div>
    <div class="signoff-role">Manager</div>
  </section>

  <div class="footer-contacts footer-phone">(616) 555-0172</div>
  <div class="footer-contacts footer-address">1840 N. Alder Ln.<br>Cedar Springs, MI 49319</div>
  <div class="footer-contacts footer-web">MorvestaLLC@gmail.com<br>www.MorvestaLLC.com</div>
</main>
</body>
</html>
```